Bref créative
Brant & Co. LLC
Commercial Real Estate/ Invesment Group/Commercial Investment Group
Simple
Thomas Verhoeven
Aquisitions/Development
Not needed
555-318-2096 not on stationary
tom@brantandcollc.example
brantandcollc.example

```html
<!DOCTYPE html>
<html lang="en">
<head>
<meta charset="utf-8">
<title>Brant &amp; Co. LLC — Business Cards</title>
<link rel="stylesheet" href="https://fonts.googleapis.com/css2?family=Open+Sans:wght@400;700&display=swap">
<style>
  :root {
    --stage: #9a9a9a;
    --stage-light: #c4c4c4;
    --card: #1b1a1a;
    --gold: #c9a04a;
    --silver: #d9d9d9;
    --ink: #ffffff;
  }
  * { margin: 0; padding: 0; box-sizing: border-box; }
  html, body { width: 1200px; height: 745px; overflow: hidden; }
  body {
    position: relative;
    background: radial-gradient(ellipse at 50% 40%, var(--stage-light), var(--stage) 75%);
    font-family: "Open Sans", Arial, sans-serif;
  }
  .card {
    position: absolute;
    width: 552px;
    height: 312px;
    background: var(--card);
    overflow: hidden;
    box-shadow: 0 4px 10px rgba(0,0,0,.35);
  }
  .card--front-gold   { left: 43px;  top: 36px; }
  .card--front-silver { left: 625px; top: 36px; }
  .card--back-gold    { left: 43px;  top: 384px; }
  .card--back-silver  { left: 625px; top: 384px; }

  .card__edges { position: absolute; inset: 0; width: 100%; height: 100%; }

  .brand {
    position: absolute;
    left: 0; right: 0;
    display: flex;
    justify-content: center;
    align-items: flex-end;
    gap: 12px;
  }
  .card--front-gold .brand, .card--front-silver .brand { top: 66px; }
  .card--back-gold .brand, .card--back-silver .brand { top: 112px; }
  .brand__mark { width: 44px; height: 44px; flex: none; }
  .brand__text { display: flex; flex-direction: column; }
  .brand__name { font-size: 27px; font-weight: 400; line-height: 1; white-space: nowrap; }
  .brand__tag { font-size: 9px; font-weight: 400; letter-spacing: .6px; margin-top: 3px; white-space: nowrap; }

  .card--front-gold .brand__name, .card--back-gold .brand__name,
  .card--front-gold .brand__tag,  .card--back-gold .brand__tag { color: var(--gold); }
  .card--front-gold .brand__mark, .card--back-gold .brand__mark { background: var(--gold); }
  .card--front-silver .brand__name, .card--back-silver .brand__name,
  .card--front-silver .brand__tag,  .card--back-silver .brand__tag { color: var(--silver); }
  .card--front-silver .brand__mark, .card--back-silver .brand__mark { background: var(--silver); }

  .person {
    position: absolute;
    top: 168px; left: 0; right: 0;
    text-align: center;
    color: var(--ink);
  }
  .person__name { font-size: 18px; font-weight: 700; line-height: 24px; }
  .person__role { font-size: 11px; line-height: 15px; }

  .contact {
    position: absolute;
    top: 230px; left: 0; right: 0;
    text-align: center;
    color: var(--ink);
    font-size: 12.5px;
    line-height: 22px;
    white-space: nowrap;
  }
  .contact__sep { margin: 0 4px; }
  .icon { width: 10px; height: 10px; vertical-align: -1px; margin-right: 3px; fill: currentColor; }
</style>
</head>
<body>

<svg width="0" height="0" style="position:absolute" aria-hidden="true">
  <defs>
    <linearGradient id="gold" x1="0" y1="0" x2="1" y2="1">
      <stop offset="0" stop-color="#a9782a"/>
      <stop offset=".45" stop-color="#ecd08a"/>
      <stop offset="1" stop-color="#b38a3a"/>
    </linearGradient>
    <linearGradient id="silver" x1="0" y1="0" x2="1" y2="1">
      <stop offset="0" stop-color="#8f8f8f"/>
      <stop offset=".45" stop-color="#f4f4f4"/>
      <stop offset="1" stop-color="#a3a3a3"/>
    </linearGradient>
  </defs>
</svg>

<section class="card card--front-gold">
  <svg class="card__edges" viewBox="0 0 552 312" preserveAspectRatio="none" aria-hidden="true">
    <path d="M0 0 H34 Q62 156 34 312 H0 Z" fill="url(#silver)"/>
    <path d="M0 0 H26 Q52 156 26 312 H0 Z" fill="url(#gold)"/>
    <path d="M552 0 H518 Q490 156 518 312 H552 Z" fill="url(#silver)"/>
    <path d="M552 0 H526 Q500 156 526 312 H552 Z" fill="url(#gold)"/>
  </svg>
  <div class="brand"><span class="brand__mark"></span><div class="brand__text"><div class="brand__name">Brant &amp; Co. LLC</div><div class="brand__tag">COMMERCIAL INVESTMENT GROUP</div></div></div>
  <div class="person"><div class="person__name">Thomas Verhoeven</div><div class="person__role">Aquisitions/Development</div></div>
  <div class="contact">
    <div><svg class="icon" viewBox="0 0 12 12"><path d="M2 1l2 0 1 3-1.5 1a6 6 0 0 0 3.5 3.5L8 7l3 1v2a1 1 0 0 1-1 1A9 9 0 0 1 1 2a1 1 0 0 1 1-1z"/></svg>555-318-2041<span class="contact__sep">|</span><svg class="icon" viewBox="0 0 12 12"><rect x="3" y="0.5" width="6" height="11" rx="1"/></svg>555-318-2096<span class="contact__sep">|</span><svg class="icon" viewBox="0 0 12 12"><rect x="1" y="4" width="10" height="6" rx="1"/><rect x="3" y="1" width="6" height="3"/></svg>555-318-2173</div>
    <div><svg class="icon" viewBox="0 0 12 12"><circle cx="6" cy="6" r="5.5"/></svg>tom@brantandcollc.example<span class="contact__sep">|</span><svg class="icon" viewBox="0 0 12 12"><circle cx="6" cy="6" r="5.5"/></svg>www.brantandcollc.example</div>
  </div>
</section>

<section class="card card--front-silver">
  <svg class="card__edges" viewBox="0 0 552 312" preserveAspectRatio="none" aria-hidden="true">
    <path d="M0 0 H34 Q62 156 34 312 H0 Z" fill="url(#gold)"/>
    <path d="M0 0 H26 Q52 156 26 312 H0 Z" fill="url(#silver)"/>
    <path d="M552 0 H518 Q490 156 518 312 H552 Z" fill="url(#gold)"/>
    <path d="M552 0 H526 Q500 156 526 312 H552 Z" fill="url(#silver)"/>
  </svg>
  <div class="brand"><span class="brand__mark"></span><div class="brand__text"><div class="brand__name">Brant &amp; Co. LLC</div><div class="brand__tag">COMMERCIAL INVESTMENT GROUP</div></div></div>
  <div class="person"><div class="person__name">Thomas Verhoeven</div><div class="person__role">Aquisitions/Development</div></div>
  <div class="contact">
    <div><svg class="icon" viewBox="0 0 12 12"><path d="M2 1l2 0 1 3-1.5 1a6 6 0 0 0 3.5 3.5L8 7l3 1v2a1 1 0 0 1-1 1A9 9 0 0 1 1 2a1 1 0 0 1 1-1z"/></svg>555-318-2041<span class="contact__sep">|</span><svg class="icon" viewBox="0 0 12 12"><rect x="3" y="0.5" width="6" height="11" rx="1"/></svg>555-318-2096<span class="contact__sep">|</span><svg class="icon" viewBox="0 0 12 12"><rect x="1" y="4" width="10" height="6" rx="1"/><rect x="3" y="1" width="6" height="3"/></svg>555-318-2173</div>
    <div><svg class="icon" viewBox="0 0 12 12"><circle cx="6" cy="6" r="5.5"/></svg>tom@brantandcollc.example<span class="contact__sep">|</span><svg class="icon" viewBox="0 0 12 12"><circle cx="6" cy="6" r="5.5"/></svg>www.brantandcollc.example</div>
  </div>
</section>

<section class="card card--back-gold">
  <svg class="card__edges" viewBox="0 0 552 312" preserveAspectRatio="none" aria-hidden="true">
    <path d="M0 0 H34 Q62 156 34 312 H0 Z" fill="url(#silver)"/>
    <path d="M0 0 H26 Q52 156 26 312 H0 Z" fill="url(#gold)"/>
    <path d="M552 0 H518 Q490 156 518 312 H552 Z" fill="url(#silver)"/>
    <path d="M552 0 H526 Q500 156 526 312 H552 Z" fill="url(#gold)"/>
  </svg>
  <div class="brand"><span class="brand__mark"></span><div class="brand__text"><div class="brand__name">Brant &amp; Co. LLC</div><div class="brand__tag">COMMERCIAL INVESTMENT GROUP</div></div></div>
</section>

<section class="card card--back-silver">
  <svg class="card__edges" viewBox="0 0 552 312" preserveAspectRatio="none" aria-hidden="true">
    <path d="M0 0 H34 Q62 156 34 312 H0 Z" fill="url(#gold)"/>
    <path d="M0 0 H26 Q52 156 26 312 H0 Z" fill="url(#silver)"/>
    <path d="M552 0 H518 Q490 156 518 312 H552 Z" fill="url(#gold)"/>
    <path d="M552 0 H526 Q500 156 526 312 H552 Z" fill="url(#silver)"/>
  </svg>
  <div class="brand"><span class="brand__mark"></span><div class="brand__text"><div class="brand__name">Brant &amp; Co. LLC</div><div class="brand__tag">COMMERCIAL INVESTMENT GROUP</div></div></div>
</section>

</body>
</html>
```